Webdesign für Sicherheitsdienst
Zielgruppe
Wir sind ein Sicherheitsdienst. Schwerpunkte: Werk- und Objektschutz, Personenschutz, Veranstaltungen und Detektei. Zielgruppe: Unternehmer, Behörden und Privatpersonen
Aufgabenstellung
Farben: Blau und weiß (wie das Logo), seriöses, edles Auftreten, wechselnde bzw. laufende Bilder einbauen, Beispiel: https://www.halvoro-tage.events/.
Hauptaugenmerk liegt für uns auf eine ordentliche, aufgeräumte, seriöse Homepage, um Kunden und Mitarbeiter zu gewinnen

```html
<!DOCTYPE html>
<html lang="de">
<head>
<meta charset="utf-8">
<title>KVR Sicherheitsdienst Nürnberg</title>
<link href="https://fonts.googleapis.com/css2?family=Poppins:wght@400;500;600;700&family=Lora:wght@400;700&display=swap" rel="stylesheet">
<style>
:root{
  --blue:#0d3a8b;
  --blue-dark:#0a2d6e;
  --white:#ffffff;
  --bg:#ffffff;
  --card:#f7f8fb;
  --text:#1d2433;
  --muted:#8a93a6;
  --map:#eceef1;
}
*{margin:0;padding:0;box-sizing:border-box}
html,body{width:1200px;height:3454px;overflow:hidden;background:var(--bg)}
body{font-family:"Lora",serif;color:var(--text);position:relative}
.page{position:absolute;left:67px;top:62px;width:1070px;height:3288px;background:var(--white);box-shadow:0 6px 24px rgba(0,0,0,.18);overflow:hidden}
.abs{position:absolute}
.h{font-family:"Poppins",sans-serif;color:var(--blue);font-weight:600;text-transform:uppercase}
.btn{position:absolute;font-family:"Poppins",sans-serif;font-size:11px;color:var(--text);border:2px solid var(--blue-dark);padding:4px 10px;display:flex;align-items:center;gap:6px;background:#fff;white-space:nowrap}
.btn.light{color:#fff;border-color:#fff;background:transparent}
.dot{width:10px;height:10px;border-radius:50%;background:currentColor;display:inline-block}
.shadow{box-shadow:0 4px 16px rgba(0,0,0,.15)}
p.body{font-size:11.5px;line-height:1.6}
.topbar{left:0;top:0;width:1070px;height:34px;background:var(--blue)}
.topbar .info{position:absolute;top:9px;font-family:"Poppins",sans-serif;font-size:11.5px;font-weight:600;color:#fff}
.social{position:absolute;top:9px;width:17px;height:17px;border:2px solid #fff;border-radius:3px}
.logo{left:74px;top:0;width:229px;height:102px;background:#fff;display:flex;flex-direction:column;align-items:center;justify-content:center;gap:4px;z-index:3}
.logo .mark{width:22px;height:22px;border-radius:50%;background:var(--blue)}
.logo .name{font-family:"Poppins",sans-serif;color:var(--blue);font-size:15px;font-weight:500}
.nav{position:absolute;top:52px;font-family:"Poppins",sans-serif;font-size:11.5px;font-weight:600;color:var(--blue)}
.hero{left:0;top:84px;width:1070px;height:560px;background:linear-gradient(120deg,#0e1a33 0%,#24406f 45%,#7d9ccc 80%,#b9cbe6 100%)}
.hero-title{left:0;top:530px;width:1070px;text-align:center;font-family:"Poppins",sans-serif;font-weight:700;font-size:44px;color:#fff;text-shadow:0 2px 6px rgba(0,0,0,.4)}
.card{position:absolute;background:#fff}
.service{background:var(--card);box-shadow:0 3px 10px rgba(0,0,0,.1);text-align:center}
.service .icon{position:absolute;left:50%;top:22px;margin-left:-36px}
.service .t{position:absolute;left:0;width:100%;top:125px;font-family:"Poppins",sans-serif;font-weight:600;font-size:14.5px;color:var(--blue);line-height:1.1}
.checks li{list-style:none;font-family:"Poppins",sans-serif;font-size:11.5px;font-weight:500;color:var(--blue);line-height:25px;padding-left:20px;position:relative}
.checks li svg{position:absolute;left:0;top:8px}
.news{box-shadow:0 3px 12px rgba(0,0,0,.1);background:#fff}
.news .img{height:172px}
.news .t{position:absolute;left:22px;top:200px;font-family:"Poppins",sans-serif;font-weight:600;font-size:14px;color:var(--text)}
.news p{position:absolute;left:22px;top:242px;width:225px;font-size:11px;line-height:1.6}
.news .more{position:absolute;left:22px;top:356px;font-family:"Poppins",sans-serif;font-size:8px;font-weight:600;color:var(--blue)}
.foot-h{font-family:"Poppins",sans-serif;font-size:11px;font-weight:600;color:var(--blue)}
.foot{font-size:11px;line-height:1.6}
.map{left:0;top:2579px;width:1070px;height:410px;background:linear-gradient(135deg,#eef0f3 0%,#e6e9ed 45%,#eef0f2 100%)}
.map-info{left:4px;top:6px;width:226px;height:82px;background:#fff;box-shadow:0 1px 4px rgba(0,0,0,.25);font-family:"Poppins",sans-serif;padding:8px 10px}
.map-info .n{font-size:9.5px;font-weight:600;color:#222}
.map-info .a{font-size:8px;color:#555;margin-top:2px}
.map-info .r{font-size:8px;color:#777;margin-top:8px}
.map-info .l{font-size:7.5px;color:#888;margin-top:6px}
.zoom{left:1022px;top:310px;width:28px;height:58px;background:#fff;box-shadow:0 1px 4px rgba(0,0,0,.3);font-family:Arial,sans-serif;font-size:20px;color:#555;text-align:center;line-height:29px}
</style>
</head>
<body>
<div class="page">
  <div class="abs topbar">
    <svg class="abs" style="left:550px;top:11px" width="12" height="12" viewBox="0 0 24 24"><path fill="#fff" d="M6.6 10.8a15 15 0 006.6 6.6l2.2-2.2c.3-.3.7-.4 1-.2 1.1.4 2.3.6 3.6.6.6 0 1 .4 1 1V20c0 .6-.4 1-1 1A17 17 0 013 4c0-.6.4-1 1-1h3.5c.6 0 1 .4 1 1 0 1.2.2 2.4.6 3.6.1.3 0 .7-.2 1z"/></svg>
    <span class="info" style="left:570px">0 800 – 555 010 0 (kostenfrei, 24h)</span>
    <span class="info" style="left:823px">JOBS / KARRIERE</span>
    <span class="social" style="left:950px"></span>
    <span class="social" style="left:975px"></span>
  </div>
  <div class="abs logo shadow"><span class="mark"></span><span class="name">KVR Sicherheitsdienst</span></div>
  <span class="nav" style="left:575px">LEISTUNGEN</span>
  <span class="nav" style="left:675px">UNTERNEHMEN</span>
  <span class="nav" style="left:792px">NEUIGKEITEN</span>
  <span class="btn" style="left:914px;top:44px;font-size:10.5px">Kontakt <span class="dot"></span></span>

  <div class="abs hero" role="img" aria-label="Sicherheitsmitarbeiter mit Taschenlampe in einem Flur"></div>
  <svg class="abs" style="left:0;top:600px" width="1070" height="345"><polygon points="0,12 1070,0 1070,306 0,340" fill="#0d3a8b"/></svg>
  <div class="abs hero-title">WIR SCHÜTZEN NÜRNBERG</div>

  <div class="card shadow" style="left:118px;top:607px;width:832px;height:351px">
    <div class="abs h" style="left:37px;top:36px;font-weight:400;font-size:24px;line-height:1.05">Herzlich willkommen<br>bei KVR Sicherheit Nürnberg</div>
    <div class="abs" style="left:37px;top:108px;width:90px;height:2px;background:var(--blue)"></div>
    <div class="abs" style="left:37px;top:127px;width:385px">
      <p class="body">Wir sind ein inhabergeführtes Unternehmen mit Verantwortungsbewusstsein für Sicherheit und Service. Durch unseren eigenen hohen Qualitätsanspruch und unsere Flexibilität haben wir seit Firmengründung ein kontinuierliches Wachstum zu verzeichnen.</p>
      <p class="body" style="margin-top:10px">Selbst kurzfristige Aufträge, beispielsweise bei Problemen mit der Alarmanlage oder bei notwendig gewordenen Brandwachen, können durch unser qualifiziertes Personal abgedeckt werden.</p>
      <p class="body" style="margin-top:10px;font-weight:700">Für Beratungs- und Informationsgespräche stehen wir Ihnen gerne zur Verfügung.</p>
    </div>
    <div class="abs" style="left:459px;top:38px;width:336px;height:276px;background:linear-gradient(180deg,#5d86c9 0%,#9fb7d8 40%,#5c7a3c 70%,#2c3a22 100%)" role="img" aria-label="Team in schwarzer Dienstkleidung vor einem Schloss"></div>
  </div>

  <div class="abs h" style="left:0;top:1050px;width:1070px;text-align:center;font-size:19px">Unsere Leistungen</div>

  <div class="card service" style="left:81px;top:1116px;width:215px;height:221px">
    <svg class="icon" width="72" height="80" viewBox="0 0 72 80" fill="none" stroke="#0d3a8b" stroke-width="2">
      <path d="M28 4v18"/><rect x="22" y="22" width="30" height="54" rx="3"/><rect x="27" y="28" width="20" height="12"/>
      <rect x="27" y="50" width="5" height="5"/><rect x="34.5" y="50" width="5" height="5"/><rect x="42" y="50" width="5" height="5"/>
      <rect x="27" y="60" width="5" height="5"/><rect x="34.5" y="60" width="5" height="5"/><rect x="42" y="60" width="5" height="5"/>
      <path d="M52 32h4v10h-4"/>
    </svg>
    <div class="t">SICHERHEITS-<br>DIENST</div><span class="btn" style="left:50px;top:172px">mehr erfahren <span class="dot"></span></span></div>
  <div class="card service" style="left:312px;top:1116px;width:214px;height:221px">
    <svg class="icon" width="72" height="80" viewBox="0 0 72 80" fill="none" stroke="#0d3a8b" stroke-width="2">
      <circle cx="20" cy="52" r="14"/><circle cx="52" cy="52" r="14"/><circle cx="20" cy="52" r="8"/><circle cx="52" cy="52" r="8"/>
      <path d="M10 42l6-14h10l4 10M62 42l-6-14H46l-4 10M30 44h12"/>
    </svg>
    <div class="t">DETEKTEI &amp;<br>OBERSERVATION</div><span class="btn" style="left:50px;top:172px">mehr erfahren <span class="dot"></span></span></div>
  <div class="card service" style="left:542px;top:1116px;width:214px;height:221px">
    <svg class="icon" width="72" height="80" viewBox="0 0 72 80" fill="none" stroke="#0d3a8b" stroke-width="2">
      <path d="M18 40h36l-5 22H23z"/><path d="M27 62l-4 14M45 62l4 14"/>
      <path d="M40 40V20l4-10h4v10l-4 20"/><path d="M28 40l-2-12h8l-2 12"/>
    </svg>
    <div class="t">SERVICE &amp;<br>HOSTESSEN</div><span class="btn" style="left:50px;top:172px">mehr erfahren <span class="dot"></span></span></div>
  <div class="card service" style="left:772px;top:1116px;width:215px;height:221px">
    <svg class="icon" width="72" height="80" viewBox="0 0 72 80" fill="none" stroke="#0d3a8b" stroke-width="2">
      <rect x="4" y="8" width="64" height="46"/><path d="M20 22h32M16 32h12M44 32h12"/>
      <circle cx="36" cy="54" r="10" fill="#f7f8fb"/><path d="M31 54l4 4 6-7"/><path d="M30 62l-2 14 8-5 8 5-2-14"/>
    </svg>
    <div class="t">SCHULUNGEN &amp;<br>AUSBILDUNG</div><span class="btn" style="left:50px;top:172px">mehr erfahren <span class="dot"></span></span></div>

  <svg class="abs" style="left:0;top:1470px" width="1070" height="390"><polygon points="0,36 1070,0 1070,360 0,384" fill="#0d3a8b"/></svg>
  <div class="card shadow" style="left:74px;top:1435px;width:561px;height:457px">
    <div class="abs h" style="left:46px;top:42px;font-size:18px">Wieso Sicherheitsdienst Nürnberg?</div>
    <p class="abs body" style="left:46px;top:98px;font-size:11px">Sie fragen sich wieso Sie gerader KVR beauftragen sollen?!<br>Ganze einfach:</p>
    <ul class="abs checks" style="left:46px;top:158px;width:480px">
      <li><svg width="13" height="10" viewBox="0 0 13 10"><path d="M1 5l4 4 7-8" stroke="#0d3a8b" stroke-width="2" fill="none"/></svg>XX Jahre Erfahrung im Sicherheitsdienst</li>
      <li><svg width="13" height="10" viewBox="0 0 13 10"><path d="M1 5l4 4 7-8" stroke="#0d3a8b" stroke-width="2" fill="none"/></svg>optimal ausgebildete und erfahrene Mitarbeiter (Ausbildung gemäß §34a der Gewerbeordnung)</li>
      <li><svg width="13" height="10" viewBox="0 0 13 10"><path d="M1 5l4 4 7-8" stroke="#0d3a8b" stroke-width="2" fill="none"/></svg>Diskretion wird bei uns groß geschrieben</li>
      <li><svg width="13" height="10" viewBox="0 0 13 10"><path d="M1 5l4 4 7-8" stroke="#0d3a8b" stroke-width="2" fill="none"/></svg>Kundenfreundlichkeit &amp; Konfliktlösung stehen im Vordergrund</li>
      <li><svg width="13" height="10" viewBox="0 0 13 10"><path d="M1 5l4 4 7-8" stroke="#0d3a8b" stroke-width="2" fill="none"/></svg>kurzfristig buchbar</li>
      <li><svg width="13" height="10" viewBox="0 0 13 10"><path d="M1 5l4 4 7-8" stroke="#0d3a8b" stroke-width="2" fill="none"/></svg>hoher Qualitätsanspruch</li>
      <li><svg width="13" height="10" viewBox="0 0 13 10"><path d="M1 5l4 4 7-8" stroke="#0d3a8b" stroke-width="2" fill="none"/></svg>hochmodernes Equipment</li>
      <li><svg width="13" height="10" viewBox="0 0 13 10"><path d="M1 5l4 4 7-8" stroke="#0d3a8b" stroke-width="2" fill="none"/></svg>große Flexibilität</li>
      <li><svg width="13" height="10" viewBox="0 0 13 10"><path d="M1 5l4 4 7-8" stroke="#0d3a8b" stroke-width="2" fill="none"/></svg>faire Preise</li>
    </ul>
  </div>
  <div class="abs h" style="left:673px;top:1592px;font-size:18px;color:#fff">Habens Sie noch Fragen?</div>
  <p class="abs body" style="left:673px;top:1644px;width:330px;color:#fff;font-size:11px">Unsere Mitarbeiter stehen Ihnen jederzeit für Fragen zur Verfügung. Nehmen Sie noch heute Kontakt zu uns auf!</p>
  <span class="btn light" style="left:673px;top:1708px">Kontakt aufnehmen <span class="dot"></span></span>

  <div class="abs h" style="left:0;top:1967px;width:1070px;text-align:center;font-size:19px">Aktuelle News</div>
  <div class="abs" style="left:490px;top:2015px;width:90px;height:2px;background:var(--blue)"></div>
  <div class="card news" style="left:118px;top:2046px;width:262px;height:378px"><div class="img" style="background:linear-gradient(180deg,#8fb0d6,#c7ccd2 60%,#8a8f94)" role="img" aria-label="Firmengebäude"></div><div class="t">NEWSBEITRAG 3</div><p>Lorem ipsum dolor sit amet, consectetuer adipiscing elit. Aenean commodo ligula eget dolor. Aenean massa. Cum sociis natoque penatibus et magnis dis parturient montes, nascetur</p><span class="more">MEHR LESEN ›</span></div>
  <div class="card news" style="left:403px;top:2046px;width:262px;height:378px"><div class="img" style="background:linear-gradient(180deg,#2e4a3a,#5d6f3a 55%,#c9d33a 75%,#3c4a5c)" role="img" aria-label="Gruppenbild des Teams in Warnwesten"></div><div class="t">NEWSBEITRAG</div><p>Lorem ipsum dolor sit amet, consectetuer adipiscing elit. Aenean commodo ligula eget dolor. Aenean massa. Cum sociis natoque penatibus et magnis dis parturient montes, nascetur</p><span class="more">MEHR LESEN ›</span></div>
  <div class="card news" style="left:688px;top:2046px;width:263px;height:378px"><div class="img" style="background:linear-gradient(120deg,#101a30,#2a4474 50%,#9fb5d8)" role="img" aria-label="Sicherheitsmitarbeiter im Flur"></div><div class="t">NEWSBEITRAG 2</div><p>Lorem ipsum dolor sit amet, consectetuer adipiscing elit. Aenean commodo ligula eget dolor. Aenean massa. Cum sociis natoque penatibus et magnis dis parturient montes, nascetur</p><span class="more">MEHR LESEN ›</span></div>
  <span class="btn" style="left:465px;top:2450px">weitere Neuigkeiten <span class="dot"></span></span>

  <div class="abs map" role="img" aria-label="Karte mit dem Standort in Nürnberg-Langwasser">
    <div class="abs map-info">
      <div class="n">KVR Sicherheitsdienst Nürnbe...</div>
      <div class="a">Lindenweg 42, 90471 Nürnberg</div>
      <div class="r">4,7 ★★★★★ &nbsp;27 Berichte</div>
      <div class="l">Größere Karte ansehen</div>
    </div>
    <svg class="abs" style="left:522px;top:154px" width="18" height="24" viewBox="0 0 10 14"><path d="M5 0a5 5 0 015 5c0 4-5 9-5 9S0 9 0 5a5 5 0 015-5z" fill="#555"/><circle cx="5" cy="5" r="2" fill="#eceef1"/></svg>
    <div class="abs" style="left:544px;top:156px;font-family:Poppins,sans-serif;font-size:9px;color:#555;line-height:1.2">KVR Sicherheitsdienst<br>Nürnberg eK</div>
    <div class="abs zoom">+<br>−</div>
  </div>

  <div class="abs" style="left:74px;top:3030px;display:flex;align-items:center;gap:6px"><span style="width:18px;height:18px;border-radius:50%;background:var(--blue)"></span><span style="font-family:Poppins,sans-serif;color:var(--blue);font-size:14px;font-weight:500">KVR Sicherheitsdienst</span></div>
  <svg class="abs" style="left:82px;top:3118px" width="10" height="12" viewBox="0 0 10 12"><path d="M5 0a4 4 0 014 4c0 3-4 8-4 8S1 7 1 4a4 4 0 014-4z" fill="#0d3a8b"/><circle cx="5" cy="4" r="1.5" fill="#fff"/></svg>
  <div class="abs foot-h" style="left:98px;top:3117px">ADRESSE</div>
  <div class="abs foot" style="left:98px;top:3138px"><b>KVR Sicherheitsdienst<br>Nürnberg e. K.</b><br>Lindenweg 42<br>90471 Nürnberg</div>
  <svg class="abs" style="left:286px;top:3118px" width="11" height="11" viewBox="0 0 24 24"><path fill="#0d3a8b" d="M6.6 10.8a15 15 0 006.6 6.6l2.2-2.2c.3-.3.7-.4 1-.2 1.1.4 2.3.6 3.6.6.6 0 1 .4 1 1V20c0 .6-.4 1-1 1A17 17 0 013 4c0-.6.4-1 1-1h3.5c.6 0 1 .4 1 1 0 1.2.2 2.4.6 3.6.1.3 0 .7-.2 1z"/></svg>
  <div class="abs foot-h" style="left:302px;top:3117px">KONTAKT</div>
  <div class="abs foot" style="left:302px;top:3138px"><b>Fon</b> 0 800 – 555 010 0<br>(kostenfrei, 24h)<br><b>Fon</b> 0911 – 555 012 30<br><b>Fax</b> 0911 – 555 012 31</div>
  <div class="abs foot-h" style="left:499px;top:3117px;line-height:2.3">LEISTUNGEN<br>UNTERNEHMEN<br>NEUIGKEITEN</div>

  <div class="card shadow" style="left:688px;top:2958px;width:307px;height:273px">
    <div class="abs h" style="left:45px;top:38px;font-size:18px;line-height:1.1">Neugierig<br>geworden?</div>
    <p class="abs body" style="left:45px;top:126px;width:220px;font-size:11px">Sollten Sie noch Fragen haben, kontaktieren Sie uns einfach unverbindlich:</p>
    <span class="btn" style="left:45px;top:200px">Kontakt aufnehmen <span class="dot"></span></span>
  </div>

  <div class="abs" style="left:0;top:3254px;width:1070px;height:34px;background:var(--blue);font-family:Poppins,sans-serif;color:#fff">
    <span class="abs" style="left:74px;top:12px;font-size:8px">© 2020 KVR SICHERHEITSDIENST NÜRNBERG | ALLE RECHTE VORBEHALTEN</span>
    <span class="abs" style="left:683px;top:11px;font-size:10px;font-weight:600">IMPRESSUM</span>
    <span class="abs" style="left:772px;top:11px;font-size:10px;font-weight:600">DATENSCHUTZ</span>
  </div>
</div>
</body>
</html>
```